Design Shopify E-Commerce Website for Men's Products

Design a Shopify website for men to sell our men's jewelry, cigar and bar accessories, and other men's products. Design should be hip, with like a rock n' roll, biker, whiskey driker flare. Name of the company is "Ironvale Locker" and website will be www.IronvaleLocker.com
Homepage will have navigation bar with three categories: Men's Jewelry, Cigar & Bar Products, Man Cave Swag
I will upload our logo, inspiration type pictures and some of the products that we sell
Theme colors should be mainly dark: black, grey, brown, gold

```html
<!DOCTYPE html>
<html lang="en">
<head>
<meta charset="utf-8">
<title>Ironvale Locker — Home</title>
<link rel="stylesheet" href="https://fonts.googleapis.com/css2?family=Noto+Serif:wght@400;700&family=Roboto:wght@400;500;700&display=swap">
<style>
:root{
  --black:#0d0c0b;
  --charcoal:#1a1918;
  --panel:#222120;
  --grey-light:#eeeff1;
  --gold:#d8b445;
  --gold-light:#f3e08a;
  --gold-deep:#b88d24;
  --brown:#6b4a0c;
  --cta-heading:#8a5a10;
  --text-dark:#1b1b1b;
  --text-muted:#666;
  --white:#ffffff;
}
*{box-sizing:border-box;margin:0;padding:0}
html,body{width:1200px;height:4096px;overflow:hidden}
body{position:relative;background:var(--black);font-family:"Roboto",sans-serif;color:var(--white)}
.abs{position:absolute}
.btn-gold{position:absolute;display:flex;align-items:center;justify-content:center;border-radius:30px;
  background:linear-gradient(180deg,var(--gold-light),var(--gold-deep));color:var(--brown);
  font-family:"Noto Serif",serif;font-weight:700;font-size:17px;box-shadow:0 0 0 2px rgba(255,255,255,.25) inset}
.arrow{position:absolute;width:46px;height:46px;border-radius:50%;display:flex;align-items:center;justify-content:center}
.arrow.prev{border:2px solid var(--gold)}
.arrow.next{background:var(--gold)}
.section-title{position:absolute;left:0;width:1200px;text-align:center;font-family:"Noto Serif",serif;font-weight:700;font-size:44px}

/* nav */
.nav-link{position:absolute;top:56px;font-family:"Noto Serif",serif;font-size:18px;color:var(--white);white-space:nowrap}
.nav-link.active,.nav-cart{color:var(--gold)}
.brand-mark{position:absolute;left:556px;top:50px;width:90px;text-align:center;font-family:"Noto Serif",serif;font-weight:700;font-size:15px;color:var(--gold);line-height:1.15}

/* hero */
.hero{left:0;top:0;width:1200px;height:671px;background:radial-gradient(ellipse at 70% 45%,#5a3216 0%,#2c1a0e 35%,#120c08 75%)}
.hero-kicker{left:113px;top:232px;font-size:34px;font-family:"Noto Serif",serif;letter-spacing:1px}
.hero-title{left:113px;top:278px;font-size:66px;font-weight:700;font-family:"Noto Serif",serif;line-height:68px}

/* categories */
.categories{left:0;top:671px;width:1200px;height:637px;background:linear-gradient(180deg,#141312,#1c1b1a 60%,#111)}
.cat-card{position:absolute;top:835px;width:236px;height:303px;border:1.5px solid #8a6f2a;background:var(--panel)}
.cat-card .thumb{position:absolute;left:40px;top:40px;width:156px;height:150px;border-radius:6px}
.cat-card .label{position:absolute;left:0;bottom:36px;width:100%;text-align:center;font-family:"Noto Serif",serif;font-size:19px}

/* about */
.about{left:0;top:1308px;width:1200px;height:652px;background:var(--grey-light)}
.about-title{left:723px;top:1448px;font-family:"Noto Serif",serif;font-weight:700;font-size:44px;color:var(--text-dark)}
.about-text{left:723px;top:1526px;width:360px;font-size:11.5px;line-height:18.5px;color:var(--text-muted)}

/* products */
.products{left:0;top:1960px;width:1200px;height:618px;background:linear-gradient(180deg,#121110,#1d1c1b)}
.product{position:absolute;top:2114px;width:236px;height:293px;background:var(--white);border-radius:4px;overflow:hidden;color:var(--text-dark);text-align:center}
.product .thumb{height:167px}
.product .name{margin-top:18px;font-weight:700;font-size:15px}
.product .desc{margin:12px auto 0;width:190px;font-size:10px;line-height:14px;color:#8a8a8a}
.product .price{margin-top:10px;font-size:15px}

/* experience */
.experience{left:0;top:2578px;width:1200px;height:493px;background:linear-gradient(90deg,#2d2a28,#4a4541 35%,#1c1a19 70%,#2a2725)}
.exp-box{left:594px;top:2670px;width:495px;height:312px;background:#1b1a19;border:1.5px solid #8a6f2a;padding:42px 44px}
.exp-box h3{font-family:"Noto Serif",serif;font-weight:700;font-size:43px;line-height:45px}
.exp-box p{margin-top:22px;font-size:11.5px;line-height:19px;color:#ddd}

/* testimonials */
.testimonials{left:0;top:3071px;width:1200px;height:482px;background:var(--white)}
.review{position:absolute;top:3222px;width:479px;height:253px;background:var(--white);box-shadow:0 4px 18px rgba(0,0,0,.1);color:var(--text-dark)}
.review .avatar{position:absolute;left:34px;top:38px;width:82px;height:82px;border-radius:50%;background:linear-gradient(135deg,#5a4a40,#c9a98a);border:3px solid #2a2a2a}
.review .who{position:absolute;left:148px;top:52px}
.review .who b{font-size:15px;font-weight:500}
.review .who small{display:block;margin-top:6px;font-size:11px}
.review .stars{display:block;margin-top:4px;color:#e6b92a;font-size:21px;letter-spacing:1px}
.review .quote{position:absolute;left:62px;top:148px;width:390px;font-size:11.5px;line-height:19px;color:#555}
.review .qmark{position:absolute;font-family:"Noto Serif",serif;font-size:40px;color:#ddd;line-height:1}

/* call to action */
.cta{left:0;top:3553px;width:1200px;height:295px;background:linear-gradient(90deg,#c09a3c,#ecd882 45%,#c9a64a 75%,#a8822c)}
.cta-title{left:0;top:3608px;width:1200px;text-align:center;font-family:"Noto Serif",serif;font-weight:700;font-size:50px;line-height:60px;color:var(--cta-heading)}
.cta-text{left:0;top:3688px;width:1200px;text-align:center;font-size:11.5px;line-height:19px;color:#3a2a10}
.btn-white{left:521px;top:3754px;width:158px;height:42px;border-radius:24px;background:var(--white);color:var(--brown);display:flex;align-items:center;justify-content:center;font-family:"Noto Serif",serif;font-weight:700;font-size:17px}

/* footer */
.footer{left:0;top:3848px;width:1200px;height:248px;background:var(--black)}
.foot-brand{left:113px;top:3880px;width:100px;font-family:"Noto Serif",serif;font-weight:700;font-size:18px;line-height:22px;color:var(--gold)}
.social{position:absolute;top:4001px;width:26px;height:26px;border-radius:50%;border:1.5px solid var(--white)}
.foot-col{position:absolute;top:3889px;font-family:"Noto Serif",serif}
.foot-col h4{font-size:17px;font-weight:700;margin-bottom:10px}
.foot-col a{display:block;font-size:14px;line-height:23px;color:var(--white);text-decoration:none}
.newsletter{left:841px;top:3925px;width:246px;height:43px;border:1.5px solid var(--gold);border-radius:24px}
.newsletter span{position:absolute;left:20px;top:14px;font-size:10px;color:#aaa;font-family:"Noto Serif",serif}
.newsletter .go{position:absolute;right:-1px;top:-1px;width:104px;height:43px;border-radius:24px;background:var(--gold);color:var(--black);display:flex;align-items:center;justify-content:center;font-family:"Noto Serif",serif;font-weight:700;font-size:15px}
.copyright{left:0;top:4068px;width:1200px;text-align:center;font-size:10.5px}
</style>
</head>
<body>

<!-- hero -->
<div class="abs hero" role="img" aria-label="Glass of whiskey and a lit cigar on a dark wooden table"></div>
<a class="nav-link active" style="left:111px">Home</a>
<a class="nav-link" style="left:192px">Features Product</a>
<a class="nav-link" style="left:369px">Shop</a>
<a class="nav-link" style="left:443px">Categories
  <svg width="12" height="8" viewBox="0 0 12 8"><path d="M1 1l5 5 5-5" stroke="#fff" stroke-width="1.6" fill="none"/></svg></a>
<div class="brand-mark">Ironvale<br>Locker</div>
<a class="nav-link" style="left:683px">Blog</a>
<a class="nav-link" style="left:753px">Contacts</a>
<svg class="abs" style="left:890px;top:55px" width="28" height="28" viewBox="0 0 28 28" fill="none" stroke="#fff" stroke-width="1.8"><circle cx="14" cy="14" r="12"/><circle cx="14" cy="11" r="4.5"/><path d="M6 22c2-4 5-5 8-5s6 1 8 5"/></svg>
<svg class="abs" style="left:958px;top:57px" width="26" height="22" viewBox="0 0 26 22" fill="none" stroke="#fff" stroke-width="1.8"><path d="M1 2h4l3 12h13l3-9H7"/><circle cx="10" cy="19" r="1.8"/><circle cx="19" cy="19" r="1.8"/></svg>
<span class="nav-link nav-cart" style="left:990px">Cart</span>
<svg class="abs" style="left:1066px;top:58px" width="22" height="22" viewBox="0 0 22 22" fill="none" stroke="#fff" stroke-width="1.8"><circle cx="9" cy="9" r="7"/><path d="M14 14l6 6"/></svg>

<div class="abs hero-kicker">WELCOME TO</div>
<div class="abs hero-title">IRONVALE<br>LOCKER</div>
<div class="btn-gold" style="left:113px;top:451px;width:162px;height:45px">Visit Now</div>

<!-- categories -->
<section class="abs categories"></section>
<h2 class="section-title" style="top:733px">Categories</h2>
<div class="arrow prev" style="left:37px;top:966px"><svg width="22" height="12" viewBox="0 0 22 12" fill="none" stroke="#d8b445" stroke-width="1.6"><path d="M21 6H2M7 1L2 6l5 5"/></svg></div>
<div class="arrow next" style="left:1118px;top:966px"><svg width="22" height="12" viewBox="0 0 22 12" fill="none" stroke="#fff" stroke-width="1.6"><path d="M1 6h19M15 1l5 5-5 5"/></svg></div>
<div class="cat-card" style="left:110px"><div class="thumb" role="img" aria-label="Silver fleur-de-lis ring" style="background:radial-gradient(circle,#8d8d8d,#2a2928 70%)"></div><div class="label">Men's Jewelry</div></div>
<div class="cat-card" style="left:359px"><div class="thumb" role="img" aria-label="Cigar resting on a glass of whiskey" style="background:radial-gradient(circle,#c97a2a,#2a2928 70%)"></div><div class="label">Cigar</div></div>
<div class="cat-card" style="left:608px"><div class="thumb" role="img" aria-label="Wooden whiskey gift crate with glasses" style="background:radial-gradient(circle,#8a4a22,#2a2928 70%)"></div><div class="label">Bar Products</div></div>
<div class="cat-card" style="left:856px"><div class="thumb" role="img" aria-label="Silver cross pendant" style="background:radial-gradient(circle,#9a9a9a,#2a2928 70%)"></div><div class="label">Man Cave Swag</div></div>
<div class="btn-gold" style="left:520px;top:1202px;width:160px;height:48px">View All</div>

<!-- about -->
<section class="abs about"></section>
<div class="abs" role="img" aria-label="Man in a suit adjusting a cufflink" style="left:113px;top:1386px;width:435px;height:498px;background:linear-gradient(135deg,#1a1a1a,#3a3a3a 45%,#d8d8d8 70%,#222)"></div>
<div class="abs" role="img" aria-label="Black and white close-up of a motorcycle engine" style="left:397px;top:1489px;width:252px;height:291px;border:4px solid #fff;background:linear-gradient(135deg,#eee,#555 40%,#ccc 60%,#222)"></div>
<div class="abs" role="img" aria-label="Faint sketch of a hand making a rock sign" style="left:965px;top:1640px;width:170px;height:320px;background:linear-gradient(180deg,rgba(0,0,0,0),rgba(0,0,0,.05))"></div>
<h2 class="abs about-title">About Us</h2>
<p class="abs about-text">Lorem ipsum dolor sit amet, consectetur adipiscing elit. Integer cursus quam quam, eu ultrices lacus semper quis. Mauris ullamcorper, ligula in iaculis ultricies, arcu erat interdum eros, sit amet pretium lacus tellus eget elit . Praesent vulputate lorem id ligula mollis lobortis. Fusce efficitur feugiat nisi. Sed tristique sem et varius molestie. Morbi luctus auctor dictum. Mauris at imperdiet dui.Quisque elementum bibendum libero, sed pharetra ligula ullamcorper at. Etiam ullamcorper vel sem sed eleifend. Cras ut nisl turpis.</p>
<div class="btn-gold" style="left:725px;top:1711px;width:157px;height:47px">Read More</div>

<!-- featured products -->
<section class="abs products"></section>
<h2 class="section-title" style="top:2018px">Featured Products</h2>
<div class="arrow prev" style="left:37px;top:2252px"><svg width="22" height="12" viewBox="0 0 22 12" fill="none" stroke="#d8b445" stroke-width="1.6"><path d="M21 6H2M7 1L2 6l5 5"/></svg></div>
<div class="arrow next" style="left:1118px;top:2252px"><svg width="22" height="12" viewBox="0 0 22 12" fill="none" stroke="#fff" stroke-width="1.6"><path d="M1 6h19M15 1l5 5-5 5"/></svg></div>
<div class="product" style="left:113px"><div class="thumb" role="img" aria-label="Red lacquered cigar humidor" style="background:radial-gradient(circle,#8a1e1e,#fff 70%)"></div><div class="name">Cigar Humidor</div><div class="desc">Lorem ipsum dolor sit amet, consectetur adipiscing elit.</div><div class="price">500.00$ – 599.00$</div></div>
<div class="product" style="left:361px"><div class="thumb" role="img" aria-label="Octagonal burgundy cigar ashtray" style="background:radial-gradient(circle,#6a1a1a,#f4f4f4 70%)"></div><div class="name">Cigarashtray</div><div class="desc">Lorem ipsum dolor sit amet, consectetur adipiscing elit.</div><div class="price">452.00$</div></div>
<div class="product" style="left:606px"><div class="thumb" role="img" aria-label="Heavy silver and gold ring" style="background:radial-gradient(circle,#8a7a4a,#fff 70%)"></div><div class="name">HeavyRing</div><div class="desc">Lorem ipsum dolor sit amet, consectetur adipiscing elit.</div><div class="price">654.00$</div></div>
<div class="product" style="left:850px"><div class="thumb" role="img" aria-label="Open wooden cigar box filled with cigars" style="background:linear-gradient(135deg,#5a3010,#c07a30 50%,#7a4218)"></div><div class="name">Wooden Cigar Box</div><div class="desc">Lorem ipsum dolor sit amet, consectetur adipiscing elit.</div><div class="price">887.00$ – 912.00$</div></div>
<div class="btn-gold" style="left:497px;top:2468px;width:207px;height:48px">View All Products</div>

<!-- experience -->
<section class="abs experience" role="img" aria-label="Man in a leather jacket seated on a motorcycle in a garage"></section>
<div class="abs exp-box">
  <h3>Ironvale Locker Experience Centers Near You</h3>
  <p>Lorem ipsum dolor sit amet, consectetur adipiscing elit, sed do eiusmod tempor incididunt ut labore et dolore magna aliqua. Quis ipsum suspendisse ultrices gravida.</p>
</div>

<!-- testimonials -->
<section class="abs testimonials"></section>
<h2 class="section-title" style="top:3125px;color:var(--text-dark)">What Our Cousmoters Say</h2>
<div class="arrow prev" style="left:37px;top:3325px"><svg width="22" height="12" viewBox="0 0 22 12" fill="none" stroke="#d8b445" stroke-width="1.6"><path d="M21 6H2M7 1L2 6l5 5"/></svg></div>
<div class="arrow next" style="left:1118px;top:3325px"><svg width="22" height="12" viewBox="0 0 22 12" fill="none" stroke="#fff" stroke-width="1.6"><path d="M1 6h19M15 1l5 5-5 5"/></svg></div>
<div class="review" style="left:111px">
  <div class="avatar" role="img" aria-label="Customer portrait"></div>
  <div class="who"><b>Dorian Vessell</b><small>Designer</small><span class="stars">★★★★★</span></div>
  <span class="qmark" style="left:30px;top:140px">“</span>
  <p class="quote">Lorem ipsum dolor sit amet, consectetur adipiscing elit, sed do eiusmod tempor incididunt ut labore et dolore magna aliqua. Quis ipsum suspendisse ultrices gravida. Risus commodo viverra maecenas accumsan lacus vel facilisis.</p>
  <span class="qmark" style="left:130px;top:208px">”</span>
</div>
<div class="review" style="left:609px">
  <div class="avatar" role="img" aria-label="Customer portrait"></div>
  <div class="who"><b>Marcus Teller</b><small>Business consultant</small><span class="stars">★★★★★</span></div>
  <span class="qmark" style="left:30px;top:140px">“</span>
  <p class="quote">Lorem ipsum dolor sit amet, consectetur adipiscing elit, sed do eiusmod tempor incididunt ut labore et dolore magna aliqua. Quis ipsum suspendisse ultrices gravida. Risus commodo viverra maecenas accumsan lacus vel facilisis.</p>
  <span class="qmark" style="left:130px;top:208px">”</span>
</div>

<!-- call to action -->
<section class="abs cta"></section>
<h2 class="abs cta-title">Your Style Journey Begins Here</h2>
<p class="abs cta-text">Lorem ipsum dolor sit amet, consectetur adipiscing elit, sed do eiusmod tempor incididunt ut labore et dolore magna aliqua.<br>Quis ipsum suspendisse ultrices gravida. Risus commodo viverra maecenas accumsan lacus vel facilisis.</p>
<div class="abs btn-white">Contat Now</div>

<!-- footer -->
<footer class="abs footer"></footer>
<div class="abs foot-brand">Ironvale Locker</div>
<span class="social" style="left:113px" aria-label="Social profile"></span>
<span class="social" style="left:146px" aria-label="Social profile"></span>
<span class="social" style="left:179px" aria-label="Social profile"></span>
<span class="social" style="left:213px" aria-label="Social profile"></span>
<div class="foot-col" style="left:313px"><h4>Shop</h4><a>Socks</a><a>Home Goods</a><a>Pins</a><a>Patches</a><a>Shop All</a></div>
<div class="foot-col" style="left:480px"><h4>About Us</h4><a>Story</a><a>Wholesale</a><a>Journal</a></div>
<div class="foot-col" style="left:652px"><h4>Help</h4><a>Contact Us</a><a>FAQs</a><a>Affiliate Program</a></div>
<div class="foot-col" style="left:841px"><h4>Subscribe To Our Newsletter</h4></div>
<div class="abs newsletter"><span>Enter your name</span><div class="go">Subscribe</div></div>
<div class="abs copyright">© 2023 Ironvale Locker</div>

</body>
</html>
```